Home Security Company Business Card

Looking for a eye catching business card that is non traditional and stands out but yet still looks professional. It should include all the pertinent information such as name, title, address, telephone, e-mail, website address should definitely stand out and then finally the logo.

Target Market(s)

Residential and Commercial accounts mostly upscale accounts

Industry/Entity Type

Security

Contact Information for Business Card

Name
Title
Address
Office #
Cell #
E-mail
Website

Font styles to use
Serif
Sans Serif

Requirements
Must have
• Logo, two sided color configuration
Nice to have
• You decide
Should not have
• There really aren't any.

```html
<!DOCTYPE html>
<html lang="en">
<head>
<meta charset="utf-8">
<title>Ironvale Security Systems – Business Card</title>
<link rel="stylesheet" href="https://fonts.googleapis.com/css2?family=Cinzel:wght@400;500&display=swap">
<style>
  :root {
    --card-white: #ffffff;
    --brand-red: #7f1000;
    --name-ink: #1f1f1f;
    --title-red: #7a1208;
    --contact-ink: #ffffff;
  }
  html, body {
    margin: 0;
    padding: 0;
    width: 1200px;
    height: 711px;
    overflow: hidden;
    background: var(--card-white);
  }
  .card {
    position: relative;
    width: 1200px;
    height: 711px;
    overflow: hidden;
    background: var(--card-white);
    font-family: "Cinzel", "Times New Roman", serif;
  }
  .card-header {
    position: absolute;
    left: 0;
    top: 0;
    width: 1200px;
    height: 238px;
    background: var(--card-white);
  }
  .brand {
    position: absolute;
    left: 115px;
    top: 94px;
    display: flex;
    align-items: center;
    gap: 16px;
  }
  .brand-mark {
    width: 42px;
    height: 42px;
    background: var(--brand-red);
  }
  .brand-name {
    margin: 0;
    font-weight: 500;
    color: var(--brand-red);
    line-height: 1.05;
  }
  .brand-name .brand-main {
    display: block;
    font-size: 31px;
    letter-spacing: 0.5px;
  }
  .brand-name .brand-sub {
    display: block;
    font-size: 14px;
    letter-spacing: 0.3px;
  }
  .person {
    position: absolute;
    right: 72px;
    top: 52px;
    text-align: right;
  }
  .person-name {
    margin: 0;
    font-weight: 400;
    font-size: 62px;
    line-height: 1;
    color: var(--name-ink);
    letter-spacing: 1px;
  }
  .person-title {
    margin: 0;
    font-weight: 400;
    font-size: 50px;
    line-height: 1;
    color: var(--title-red);
    letter-spacing: 1px;
  }
  .contact-band {
    position: absolute;
    left: 0;
    top: 238px;
    width: 1200px;
    height: 473px;
    background: var(--brand-red);
  }
  .contact-list {
    list-style: none;
    margin: 0;
    padding: 0;
    color: var(--contact-ink);
    font-weight: 400;
    line-height: 1;
  }
  .contact-line {
    position: absolute;
    left: 96px;
    white-space: nowrap;
    letter-spacing: 1.5px;
  }
  .line-tollfree { top: 40px;  font-size: 46px; }
  .line-mobile   { top: 108px; font-size: 46px; }
  .line-email    { top: 166px; font-size: 43px; }
  .line-street   { top: 226px; font-size: 45px; }
  .line-city     { top: 290px; font-size: 45px; }
  .line-web      { top: 358px; font-size: 45px; }
</style>
</head>
<body>
  <main class="card">
    <header class="card-header">
      <div class="brand">
        <span class="brand-mark"></span>
        <p class="brand-name">
          <span class="brand-main">IRONVALE</span>
          <span class="brand-sub">SECURITY SYSTEMS INC.</span>
        </p>
      </div>
      <div class="person">
        <h1 class="person-name">Mara Lind</h1>
        <p class="person-title">President</p>
      </div>
    </header>
    <section class="contact-band">
      <ul class="contact-list">
        <li class="contact-line line-tollfree">toll free: 1.800.555.0100</li>
        <li class="contact-line line-mobile">mobile: 617.555.0142</li>
        <li class="contact-line line-email">info@ironvalesecure.net</li>
        <li class="contact-line line-street">123 Harbor Point Ave</li>
        <li class="contact-line line-city">Milford, MA 01757</li>
        <li class="contact-line line-web">www.ironvalesecure.net</li>
      </ul>
    </section>
  </main>
</body>
</html>
```